Demo Screens Needed for Recruiting with AI App

We are in the process of raising money for our startup called KelvoraLink. We need demos to show investors what we're trying to do with images. We really love the simplicity and modern look of the Pivlo App and want something similar. We will have the "swipe" functionality similar to Flarvi as well. The sample images I've attached are only for caregivers but long term this will be for all industries. There will also be a rewards page for loyalty membership. The current landing page is www.kelvoralink-demo.com. That will show you the color scheme and logo.

```html
<!DOCTYPE html>
<html lang="en">
<head>
<meta charset="utf-8">
<title>KelvoraLink — App Screens</title>
<link rel="stylesheet" href="https://fonts.googleapis.com/css2?family=Inter:wght@400;500;600&family=Montserrat:wght@300&display=swap">
<style>
:root{
  --board:#4b1f9e;
  --ink:#000;
  --accent:#4a1fa6;
  --accent-text:#4a22b0;
  --text:#1d1d24;
  --muted:#5f5f6b;
  --line:#d9d9df;
  --chip:#ececf0;
  --star:#f3b400;
  --online:#23a455;
  --white:#fff;
  --pill:#5d6066;
}
*{box-sizing:border-box;margin:0;padding:0}
html,body{width:1200px;height:853px;overflow:hidden}
body{background:var(--board);font-family:"Inter",sans-serif;color:var(--text);position:relative}
.brand-band{position:absolute;left:0;top:0;width:1200px;height:153px;background:var(--ink);display:flex;align-items:center;justify-content:center}
.brand-name{font-family:"Montserrat",sans-serif;font-weight:300;font-size:36px;letter-spacing:4px;color:var(--white);text-transform:uppercase}
.screen{position:absolute;top:235px;width:258px;height:559px;border-radius:24px;overflow:hidden;background:var(--white)}
.screen--welcome{left:19px;background:linear-gradient(160deg,#3a3d40 0%,#23262a 45%,#15171a 100%)}
.screen--discover{left:320px}
.screen--find{left:622px}
.screen--profile{left:922px}
.abs{position:absolute}
.status{position:absolute;top:10px;left:14px;right:14px;display:flex;justify-content:space-between;align-items:center;font-size:10px;font-weight:600}
.status svg{display:block}
.screen--welcome .status{color:var(--white)}
.photo{position:absolute;background:linear-gradient(180deg,#48603a 0%,#5d7a4a 35%,#7a7468 70%,#3e4a33 100%)}
.photo--family{inset:0;background:radial-gradient(ellipse at 30% 35%,#6b5a4c 0%,#3a3632 40%,#1e2022 80%)}
.welcome-logo{top:60px;left:0;right:0;text-align:center;font-family:"Montserrat",sans-serif;font-weight:300;font-size:21px;letter-spacing:2px;color:var(--white);text-transform:uppercase}
.welcome-title{top:307px;left:0;right:0;text-align:center;color:var(--white);font-size:15.5px;font-weight:600}
.welcome-sub{top:338px;left:40px;right:40px;text-align:center;color:#e6e6e6;font-size:10.5px;line-height:1.25}
.btn{position:absolute;display:flex;align-items:center;justify-content:center;border-radius:22px;font-size:10.5px;color:var(--white);white-space:nowrap}
.btn--primary{background:var(--accent)}
.btn--ghost{border:1px solid var(--white)}
.header{position:absolute;top:44px;left:20px;right:20px;display:flex;align-items:center;justify-content:space-between}
.header h1{font-size:17px;font-weight:500;color:var(--accent-text);flex:1;text-align:center;white-space:nowrap}
.lede{position:absolute;top:70px;left:20px;right:20px;font-size:10.5px;line-height:1.2;color:var(--muted)}
.tag{background:var(--white);color:var(--accent-text);font-size:10.5px;padding:2px 5px;display:inline-flex;gap:3px;align-items:center;white-space:nowrap}
.card-name{color:var(--white);font-size:12px;font-weight:600}
.round-btn{position:absolute;width:32px;height:32px;border-radius:50%;display:flex;align-items:center;justify-content:center}
.section-title{font-size:12px;font-weight:500;color:var(--accent-text);white-space:nowrap}
.body-copy{font-size:10.5px;line-height:1.2;color:var(--muted)}
.nav{position:absolute;left:0;right:0;bottom:0;height:71px;background:var(--ink);display:flex;justify-content:space-around;padding:0 4px;align-items:flex-start;padding-top:14px}
.nav-item{width:42px;height:28px;border-radius:14px;display:flex;align-items:center;justify-content:center;color:var(--white);font-weight:600;font-size:14px}
.nav-item.is-active{background:var(--pill)}
.home-mark{width:9px;height:9px;background:currentColor}
.home-bar{position:absolute;bottom:10px;left:84px;width:90px;height:3px;border-radius:2px;background:#3a3a3a}
.search{top:116px;left:20px;right:20px;height:22px;border-radius:11px;background:var(--chip);display:flex;align-items:center;gap:6px;padding-left:11px;font-size:10.5px;color:var(--muted)}
.filter-row{top:149px;left:20px;right:20px;display:flex;justify-content:space-between;font-size:10.5px;color:var(--muted)}
.chips{top:168px;left:20px;right:20px;display:flex;gap:4px}
.chip{background:var(--chip);font-size:10px;color:var(--muted);padding:2px 4px;display:flex;gap:2px;align-items:center;white-space:nowrap}
.result-count{top:206px;left:20px;font-size:10.5px;font-weight:600;color:var(--text)}
.result{position:absolute;left:20px;right:20px}
.result .thumb{position:absolute;left:0;top:0;width:43px;height:43px}
.result .meta{position:absolute;left:53px;top:0}
.name-line{display:flex;align-items:center;gap:12px}
.name-line b{font-weight:500;color:var(--accent-text);font-size:12px}
.online{font-size:10.5px;color:var(--muted);display:flex;align-items:center;gap:3px}
.online::before{content:"";width:6px;height:6px;border-radius:50%;background:var(--online)}
.loc{font-size:10.5px;color:var(--muted);display:flex;align-items:center;gap:2px;margin-top:3px}
.stars{display:flex;align-items:center;gap:1px;font-size:10.5px;color:var(--muted);margin-top:3px}
.stars span{margin-left:5px}
.divider{position:absolute;left:20px;right:20px;height:1px;background:var(--line)}
.facts{position:absolute;top:121px;left:20px;right:20px;list-style:none}
.facts li{display:flex;align-items:center;gap:7px;font-size:10.5px;color:var(--muted);height:21px}
</style>
</head>
<body>
<svg width="0" height="0" style="position:absolute" aria-hidden="true">
  <defs>
    <symbol id="i-star" viewBox="0 0 24 24"><path d="M12 2.5l2.9 6 6.6.8-4.9 4.5 1.3 6.5L12 17l-5.9 3.3 1.3-6.5-4.9-4.5 6.6-.8z"/></symbol>
    <symbol id="i-user" viewBox="0 0 24 24"><circle cx="12" cy="8" r="4" fill="none" stroke="currentColor" stroke-width="1.8"/><path d="M4 21c0-4.4 3.6-7 8-7s8 2.6 8 7" fill="none" stroke="currentColor" stroke-width="1.8"/></symbol>
    <symbol id="i-search" viewBox="0 0 24 24"><circle cx="11" cy="11" r="7" fill="none" stroke="currentColor" stroke-width="1.8"/><path d="M16 16l5 5" stroke="currentColor" stroke-width="1.8"/></symbol>
    <symbol id="i-chat" viewBox="0 0 24 24"><path d="M4 4h16v12H9l-5 4z" fill="none" stroke="currentColor" stroke-width="1.8" stroke-linejoin="round"/></symbol>
    <symbol id="i-pin" viewBox="0 0 24 24"><path d="M12 2a7 7 0 0 0-7 7c0 5 7 13 7 13s7-8 7-13a7 7 0 0 0-7-7zm0 9.5A2.5 2.5 0 1 1 12 6.5a2.5 2.5 0 0 1 0 5z"/></symbol>
    <symbol id="i-back" viewBox="0 0 24 24"><path d="M20 12H5m6-6l-6 6 6 6" fill="none" stroke="currentColor" stroke-width="1.8"/></symbol>
    <symbol id="i-more" viewBox="0 0 24 24"><circle cx="5" cy="12" r="2"/><circle cx="12" cy="12" r="2"/><circle cx="19" cy="12" r="2"/></symbol>
    <symbol id="i-status" viewBox="0 0 44 10"><rect x="0" y="6" width="2" height="4"/><rect x="3" y="4" width="2" height="6"/><rect x="6" y="2" width="2" height="8"/><rect x="9" y="0" width="2" height="10"/><path d="M14 3.5a7 7 0 0 1 10 0l-1.2 1.2a5.3 5.3 0 0 0-7.6 0zM16.4 6a3.6 3.6 0 0 1 5.2 0L19 8.6z"/><rect x="28" y="1" width="14" height="8" rx="2"/></symbol>
    <symbol id="i-x" viewBox="0 0 24 24"><path d="M6 6l12 12M18 6L6 18" stroke="currentColor" stroke-width="2.4" fill="none"/></symbol>
    <symbol id="i-check" viewBox="0 0 24 24"><path d="M5 12.5l4.5 4.5L19 7.5" stroke="currentColor" stroke-width="2.6" fill="none"/></symbol>
  </defs>
</svg>

<header class="brand-band"><span class="brand-name">KelvoraLink</span></header>

<!-- Welcome -->
<section class="screen screen--welcome">
  <div class="photo photo--family" role="img" aria-label="Photo of a smiling boy and his grandmother facing each other"></div>
  <div class="status"><span>9:41</span><svg width="44" height="10" fill="currentColor"><use href="#i-status"/></svg></div>
  <div class="abs welcome-logo">KelvoraLink</div>
  <div class="abs welcome-title">Welcome to KelvoraLink</div>
  <div class="abs welcome-sub">Unlocking the power of meaningful connections</div>
  <div class="btn btn--primary" style="top:389px;left:20px;width:218px;height:37px">Create account</div>
  <div class="btn btn--ghost" style="top:437px;left:20px;width:218px;height:37px">Sign in</div>
  <div class="home-bar" style="background:#2c2c30"></div>
</section>

<!-- Discover -->
<section class="screen screen--discover">
  <div class="status"><span>9:41</span><svg width="44" height="10" fill="currentColor"><use href="#i-status"/></svg></div>
  <div class="header">
    <svg width="16" height="16" color="#555"><use href="#i-back"/></svg>
    <h1>Discover your tribe</h1>
    <svg width="16" height="16" fill="#555"><use href="#i-more"/></svg>
  </div>
  <p class="lede">Swipe right to connect, left to pass. Make meaningful connections with those who align with your values.</p>
  <div class="photo" style="top:128px;left:0;width:258px;height:260px" role="img" aria-label="Photo of a caregiver in a cap sitting on a park bench"></div>
  <div class="abs card-name" style="top:140px;left:20px">Rena C.</div>
  <div class="abs" style="top:158px;left:20px"><span class="tag"><svg width="10" height="10" fill="currentColor" viewBox="0 0 24 24"><path d="M12 21s-8-5.3-8-11a4.5 4.5 0 0 1 8-2.8A4.5 4.5 0 0 1 20 10c0 5.7-8 11-8 11z"/></svg>Elderly Care, Nursing</span></div>
  <div class="round-btn" style="top:339px;left:20px;background:var(--white);color:#bbb"><svg width="18" height="18"><use href="#i-x"/></svg></div>
  <div class="round-btn" style="top:339px;left:206px;background:var(--accent);color:var(--white)"><svg width="18" height="18"><use href="#i-check"/></svg></div>
  <div class="abs section-title" style="top:408px;left:20px">One thing I prioritize in childcare is</div>
  <p class="abs body-copy" style="top:425px;left:20px;right:20px">Creating a fun and engaging atmosphere where children can explore, play, and express themselves creatively.</p>
  <nav class="nav">
    <div class="nav-item is-active" aria-label="Home"><span class="home-mark"></span></div>
    <div class="nav-item"><svg width="16" height="16" fill="none" stroke="currentColor" stroke-width="1.8"><use href="#i-star"/></svg></div>
    <div class="nav-item"><svg width="16" height="16"><use href="#i-user"/></svg></div>
    <div class="nav-item"><svg width="16" height="16"><use href="#i-search"/></svg></div>
    <div class="nav-item"><svg width="16" height="16"><use href="#i-chat"/></svg></div>
  </nav>
  <div class="home-bar"></div>
</section>

<!-- Find -->
<section class="screen screen--find">
  <div class="status"><span>9:41</span><svg width="44" height="10" fill="currentColor"><use href="#i-status"/></svg></div>
  <div class="header">
    <svg width="16" height="16" color="#555"><use href="#i-back"/></svg>
    <h1>Find Connections</h1>
    <svg width="16" height="16" fill="#555"><use href="#i-more"/></svg>
  </div>
  <p class="lede">Filter by industry, location, and expertise to find exactly who you’re looking for.</p>
  <div class="abs search"><svg width="11" height="11" color="#333"><use href="#i-search"/></svg>Search</div>
  <div class="abs filter-row"><span>▼ Filters (3)</span><span>Clear all</span></div>
  <div class="abs chips"><span class="chip">Larkmoor, CA ×</span><span class="chip">&gt;$25/hr ×</span><span class="chip">Full-time ×</span></div>
  <div class="abs result-count">Showing all results (53)</div>
  <div class="result" style="top:241px">
    <div class="thumb photo" role="img" aria-label="Profile photo of caregiver Rena"></div>
    <div class="meta">
      <div class="name-line"><b>Rena C.</b><span class="online">Active today</span></div>
      <div class="loc"><svg width="8" height="8" fill="currentColor"><use href="#i-pin"/></svg>Larkmoor, CA</div>
      <div class="stars"><svg width="12" height="12" fill="var(--star)"><use href="#i-star"/></svg><svg width="12" height="12" fill="var(--star)"><use href="#i-star"/></svg><svg width="12" height="12" fill="var(--star)"><use href="#i-star"/></svg><svg width="12" height="12" fill="var(--star)"><use href="#i-star"/></svg><svg width="12" height="12" fill="var(--star)"><use href="#i-star"/></svg><span>(62 reviews)</span></div>
    </div>
  </div>
  <div class="abs section-title" style="top:295px;left:20px;font-size:11px">One thing I prioritize in childcare is</div>
  <p class="abs body-copy" style="top:311px;left:20px;right:20px">Creating a fun and engaging atmosphere where children can explore, play, and express themselves creatively.</p>
  <div class="divider" style="top:358px"></div>
  <div class="result" style="top:370px">
    <div class="thumb photo" style="background:linear-gradient(180deg,#8a8478,#4e4a44)" role="img" aria-label="Profile photo of caregiver Mirela"></div>
    <div class="meta">
      <div class="name-line"><b>Mirela T.</b><span class="online">Active today</span></div>
      <div class="loc"><svg width="8" height="8" fill="currentColor"><use href="#i-pin"/></svg>Fenwick Bay, CA</div>
      <div class="stars"><svg width="12" height="12" fill="var(--star)"><use href="#i-star"/></svg><svg width="12" height="12" fill="var(--star)"><use href="#i-star"/></svg><svg width="12" height="12" fill="var(--star)"><use href="#i-star"/></svg><svg width="12" height="12" fill="var(--star)"><use href="#i-star"/></svg><svg width="12" height="12" fill="var(--star)"><use href="#i-star"/></svg><span>(35 reviews)</span></div>
    </div>
  </div>
  <div class="abs section-title" style="top:424px;left:20px;font-size:11px">When it comes to meal prep, I excel at</div>
  <p class="abs body-copy" style="top:440px;left:20px;right:20px">Making themed dinners such as Meatless Mondays and Taco Tuesdays</p>
  <div class="divider" style="top:474px"></div>
  <nav class="nav">
    <div class="nav-item" aria-label="Home"><span class="home-mark"></span></div>
    <div class="nav-item"><svg width="16" height="16" fill="none" stroke="currentColor" stroke-width="1.8"><use href="#i-star"/></svg></div>
    <div class="nav-item"><svg width="16" height="16"><use href="#i-user"/></svg></div>
    <div class="nav-item is-active"><svg width="16" height="16"><use href="#i-search"/></svg></div>
    <div class="nav-item"><svg width="16" height="16"><use href="#i-chat"/></svg></div>
  </nav>
  <div class="home-bar"></div>
</section>

<!-- Profile -->
<section class="screen screen--profile">
  <div class="status"><span>9:41</span><svg width="44" height="10" fill="currentColor"><use href="#i-status"/></svg></div>
  <div class="header">
    <svg width="16" height="16" color="#555"><use href="#i-back"/></svg>
    <h1>Rena Calloway</h1>
    <svg width="16" height="16" fill="#555"><use href="#i-more"/></svg>
  </div>
  <div class="abs" style="top:70px;left:20px;right:20px;display:flex;justify-content:space-between;font-size:10.5px;color:var(--muted)">
    <span class="loc" style="margin:0"><svg width="9" height="9" fill="currentColor"><use href="#i-pin"/></svg>Larkmoor, CA</span><span>$25-35/hr</span>
  </div>
  <div class="abs stars" style="top:87px;left:20px"><svg width="12" height="12" fill="var(--star)"><use href="#i-star"/></svg><svg width="12" height="12" fill="var(--star)"><use href="#i-star"/></svg><svg width="12" height="12" fill="var(--star)"><use href="#i-star"/></svg><svg width="12" height="12" fill="var(--star)"><use href="#i-star"/></svg><svg width="12" height="12" fill="var(--star)"><use href="#i-star"/></svg><span>(62 reviews)</span></div>
  <ul class="facts">
    <li><svg width="14" height="14" fill="none" stroke="#555" stroke-width="1.6" viewBox="0 0 24 24"><rect x="3" y="7" width="18" height="13" rx="2"/><path d="M9 7V4h6v3M9 7v13M15 7v13"/></svg>10+ years experience</li>
    <li><svg width="14" height="14" color="#555"><use href="#i-chat"/></svg>English, Spanish, Mandarin</li>
    <li><svg width="14" height="14" fill="none" stroke="#555" stroke-width="1.6" viewBox="0 0 24 24"><circle cx="12" cy="12" r="9"/><path d="M8 14c1 1.5 2.3 2 4 2s3-.5 4-2"/><circle cx="9" cy="10" r=".8" fill="#555"/><circle cx="15" cy="10" r=".8" fill="#555"/></svg>0-11 mos, 1-3 yrs, 4-5 yrs</li>
    <li><svg width="14" height="14" fill="none" stroke="#555" stroke-width="1.6" viewBox="0 0 24 24"><circle cx="9" cy="8" r="3.5"/><path d="M2 20c0-4 3-6 7-6s7 2 7 6M16 4.5a3.5 3.5 0 0 1 0 7M18 14c2.5.6 4 2.6 4 6"/></svg>CPR trained, special needs care</li>
    <li><svg width="14" height="14" fill="none" stroke="#555" stroke-width="1.6" viewBox="0 0 24 24"><circle cx="12" cy="12" r="9"/><path d="M12 7v5l3 2"/></svg>Full time and part-time roles</li>
  </ul>
  <div class="photo" style="top:232px;left:0;width:258px;height:262px" role="img" aria-label="Photo of caregiver Rena wearing a cap in a park"></div>
  <div class="btn btn--primary" style="top:433px;left:20px;width:115px;height:34px">Send a message</div>
  <div class="btn btn--ghost" style="top:433px;left:147px;width:91px;height:34px">Save profile</div>
  <nav class="nav">
    <div class="nav-item" aria-label="Home"><span class="home-mark"></span></div>
    <div class="nav-item is-active"><svg width="16" height="16" fill="none" stroke="currentColor" stroke-width="1.8"><use href="#i-star"/></svg></div>
    <div class="nav-item"><svg width="16" height="16"><use href="#i-user"/></svg></div>
    <div class="nav-item"><svg width="16" height="16"><use href="#i-search"/></svg></div>
    <div class="nav-item"><svg width="16" height="16"><use href="#i-chat"/></svg></div>
  </nav>
  <div class="home-bar"></div>
</section>
</body>
</html>
```